We are launching an Internet project called "Tembrio - Quick Visits". It will be available online from 1st of July 2015 at https://bookly-visits.com.au/
This is an online booking tool for services like doctors, hairdressers, electricians etc. So any short service within a day. It also can be used for business appointments with lawyers, accountants and so on.
So our part is to make communication between businesses and their customers easier and simpler. using our tool businesses are getting a tool which allows them to accept bookings 24/7, customers can make bookings any time they want even outside business hours. Also it reduces queue of customers on hold on the phone.
As our product is just started at this stage we are looking for marketing materials targeting business owners and administrators to grow our database of services to offer to the clients.
The flyer colour scheme should match website colours (white and blue, may be add a bit of soft orange). The design should attract businesses to sigh up for our services. The key points are:
1. Availability 24/7
2. Letting focus on job rather than booking management
3. Less lost clients from queue 'on hold'

Industry/Entity Type

Internet

```html
<!DOCTYPE html>
<html lang="en">
<head>
<meta charset="utf-8">
<title>Tembrio - Get Booked Smarter</title>
<link rel="stylesheet" href="https://fonts.googleapis.com/css2?family=Maven+Pro:wght@500;600&family=Source+Sans+3:wght@400;600&display=swap">
<style>
  :root {
    --page-bg: #e9e6e2;
    --paper: #ffffff;
    --brand-blue: #35a0d6;
    --footer-blue: #2f9fd0;
    --ink: #2e2e30;
    --soft-peach: rgba(238, 214, 196, 0.62);
    --peach-solid: #ecd6c6;
    --tag-peach: #f3dccb;
    --photo-light: #f4f7fa;
    --photo-mid: #c9d5e0;
    --photo-skin: #e6c9b4;
  }
  * { box-sizing: border-box; margin: 0; padding: 0; }
  html, body { width: 1200px; height: 1000px; overflow: hidden; }
  body {
    background: var(--page-bg);
    font-family: "Source Sans 3", Arial, sans-serif;
    position: relative;
  }
  .flyer {
    position: absolute;
    left: 264px; top: 26px;
    width: 672px; height: 948px;
    background: var(--paper);
    overflow: hidden;
  }
  .hero-photo {
    position: absolute;
    left: 0; top: 90px;
    width: 672px; height: 640px;
    background:
      radial-gradient(ellipse 260px 200px at 470px 230px, var(--photo-skin) 0%, rgba(230,201,180,0) 100%),
      radial-gradient(ellipse 420px 260px at 170px 430px, var(--photo-mid) 0%, rgba(201,213,224,0) 100%),
      linear-gradient(180deg, var(--paper) 0%, var(--photo-light) 20%, #dfe6ee 55%, var(--photo-light) 82%, var(--paper) 100%);
  }
  .title {
    position: absolute;
    left: 0; top: 57px; width: 672px;
    text-align: center;
    font-family: "Maven Pro", Arial, sans-serif;
    font-weight: 500;
    font-size: 29px;
    letter-spacing: 1px;
    color: var(--brand-blue);
  }
  .intro-band {
    position: absolute;
    left: 0; top: 151px;
    width: 672px; height: 128px;
    background: var(--soft-peach);
    padding: 11px 0 0 30px;
    font-size: 16.5px;
    line-height: 22px;
    color: var(--ink);
  }
  .intro-band .line { display: block; white-space: nowrap; }
  .features {
    position: absolute;
    left: 90px; top: 319px;
    width: 492px; height: 210px;
    background: rgba(240, 226, 216, 0.45);
    border-radius: 6px;
    padding: 10px 0 0 9px;
    color: var(--ink);
  }
  .features h2 {
    font-weight: 400;
    font-size: 21px;
    margin-bottom: 14px;
  }
  .features ul { list-style: none; }
  .features li {
    position: relative;
    padding-left: 26px;
    font-size: 18px;
    line-height: 30px;
    white-space: nowrap;
  }
  .features li::before {
    content: "";
    position: absolute;
    left: 5px; top: 10px;
    width: 10px; height: 10px;
    border-radius: 50%;
    background: var(--brand-blue);
  }
  .audience {
    position: absolute;
    top: 622px;
    width: 300px;
    text-align: center;
    color: var(--brand-blue);
    font-size: 15.5px;
    line-height: 22px;
  }
  .audience--business { left: 16px; }
  .audience--customer { left: 356px; }
  .audience h3 {
    display: inline-block;
    background: var(--tag-peach);
    border-radius: 9px;
    padding: 1px 9px;
    font-weight: 600;
    font-size: 16px;
    line-height: 28px;
    margin-bottom: 6px;
  }
  .footer-stripe {
    position: absolute;
    left: 0; top: 884px;
    width: 672px; height: 8px;
    background: var(--peach-solid);
  }
  .footer {
    position: absolute;
    left: 0; top: 892px;
    width: 672px; height: 56px;
    background: var(--footer-blue);
    color: #ffffff;
  }
  .brand-name {
    position: absolute;
    left: 31px; top: 14px;
    font-weight: 600;
    font-size: 20px;
  }
  .site-url {
    position: absolute;
    right: 30px; top: 15px;
    font-size: 17px;
  }
</style>
</head>
<body>
  <main class="flyer">
    <div class="hero-photo" role="img" aria-label="Photo of a hand typing on a laptop keyboard and touchpad in soft light blue tones"></div>

    <h1 class="title">Tembrio - Get Booked Smarter</h1>

    <p class="intro-band">
      <span class="line">Tembrio or Quick Visits is an online appointment management system which</span>
      <span class="line">is dedicated to bring together businesses and their customers. Tembrio allows clients</span>
      <span class="line">to book services and make appointments any time from everywhere over internet.</span>
      <span class="line">We provide both businesses and customers with easy and convenient appointment</span>
      <span class="line">management tool available 24/7</span>
    </p>

    <section class="features">
      <h2>Key features</h2>
      <ul>
        <li>Make your business available for booking 24/7.</li>
        <li>Reduce number of calls ‘on hold’ and missed clients.</li>
        <li>Manage your appointments online from any device.</li>
        <li>Receive payments online to secure your appointments.</li>
        <li>Let you focus on work rather than booking management</li>
      </ul>
    </section>

    <section class="audience audience--business">
      <h3>For businesses</h3>
      <p>No software installations required.<br>
      Booking widget for existing web sites.<br>
      Listing in our public catalog.<br>
      Online payments to secure your<br>appointments.<br>
      Availability for booking 24/7.<br>
      Email support available 7 days.</p>
    </section>

    <section class="audience audience--customer">
      <h3>For customers</h3>
      <p>Flexible services search.<br>
      No more waiting ‘On Hold’ on the phone<br>to make booking.<br>
      Services available 24/7 for booking.<br>
      Online payments. No more worries about<br>how to pay cas or card.<br>
      Flexible appointment management tools<br>for time changes and cancellations.</p>
    </section>

    <div class="footer-stripe"></div>
    <footer class="footer">
      <span class="brand-name">Tembrio</span>
      <span class="site-url">www.tembrio-visits.com.au</span>
    </footer>
  </main>
</body>
</html>
```